Saffron Lantern Court Business Card

I am looking for a business card desgined for my restaurant. It is an Indian restaurant, we are looking for something thats modern, yet traditional with the indian culture, we are looking for colors that match our logo. The logo is a design of the building with the name of the restaurant. for more information on the restaurant go to www.saffronlanterncourt.example

Industry/Entity Type

Indian Restaurant

Contact Information for Business Card

we are looking for somthing thats modern, yet traditional with the indian culture, we are looking for colors that match our logo. The logo is a design of the building with the name of the restaurant. for more information on the restaurant go to www.saffronlanterncourt.example

Requirements
Must have
• The logo that is attached,
• Name: Harvinder Oberoi,
• address of the restaurant: 7328 West Larkspur Rd, Copperfield, Arizona, 85099
• Phone: (602) 555-0147
• Fax: (602) 555-0193
• Restaurant Catering Banquet
• Website: www.SaffronLanternCourt.example
Nice to have
• wanted to get something that goes with the theme of the restaurant, which is traditional but also keep a very professional and modern touch

```html
<!DOCTYPE html>
<html lang="en">
<head>
<meta charset="utf-8">
<title>Saffron Lantern Court Business Card</title>
<link rel="stylesheet" href="https://fonts.googleapis.com/css2?family=Raleway:wght@400;500;700&display=swap">
<style>
  :root {
    --backdrop: #2b2b2d;
    --card: #000000;
    --orange: #f26b21;
    --crimson: #b3202a;
    --brand: #e2472c;
    --white: #ffffff;
    --rule: #8a8a8a;
  }
  html, body {
    margin: 0;
    width: 1200px;
    height: 900px;
    overflow: hidden;
    background: var(--backdrop);
    font-family: "Raleway", Arial, sans-serif;
  }
  .stage { position: relative; width: 1200px; height: 900px; }
  .card {
    position: absolute;
    width: 600px;
    height: 343px;
    background: var(--card);
    border-radius: 18px;
    overflow: hidden;
    box-shadow: 0 18px 40px rgba(0,0,0,.55);
  }
  .card-front { left: 70px; top: 80px; }
  .card-back { left: 530px; top: 470px; }
  .card-shapes { position: absolute; inset: 0; }

  .brand-name {
    position: absolute;
    margin: 0;
    color: var(--brand);
    font-weight: 700;
    text-transform: uppercase;
    line-height: 1.05;
    letter-spacing: 2px;
    text-align: center;
  }
  .card-front .brand-name { left: 190px; top: 92px; font-size: 36px; }
  .card-back .brand-name { left: 40px; top: 60px; font-size: 26px; }

  .website {
    margin: 0;
    color: var(--white);
    font-size: 15px;
    font-weight: 500;
  }
  .website .accent { color: var(--orange); }
  .card-front .website { position: absolute; right: 34px; top: 222px; }

  .holder-name {
    position: absolute;
    right: 36px;
    top: 64px;
    margin: 0;
    color: var(--orange);
    font-size: 20px;
    font-weight: 700;
    letter-spacing: 1px;
    text-transform: uppercase;
  }
  .holder-rule {
    position: absolute;
    left: 190px;
    right: 30px;
    top: 96px;
    height: 1px;
    background: var(--rule);
  }
  .contact-rule {
    position: absolute;
    left: 30px;
    width: 330px;
    top: 186px;
    height: 1px;
    background: var(--rule);
  }
  .contact {
    position: absolute;
    left: 40px;
    top: 196px;
    margin: 0;
    color: var(--white);
    font-size: 15px;
    line-height: 21px;
    font-style: normal;
  }
  .contact-line { display: flex; align-items: center; gap: 8px; }
  .contact-line svg { width: 12px; height: 12px; fill: var(--orange); flex: none; }
</style>
</head>
<body>
<main class="stage">

  <section class="card card-front" aria-label="Card front">
    <svg class="card-shapes" viewBox="0 0 600 343" aria-hidden="true">
      <polygon points="0,300 270,284 320,296 0,343" fill="var(--orange)"/>
      <polygon points="320,296 600,250 600,261 332,304" fill="var(--crimson)"/>
    </svg>
    <h1 class="brand-name">Saffron<br>Lantern<br>Court</h1>
    <p class="website">www.<span class="accent">SaffronLanternCourt</span>.example</p>
  </section>

  <section class="card card-back" aria-label="Card back">
    <svg class="card-shapes" viewBox="0 0 600 343" aria-hidden="true">
      <polygon points="378,248 600,190 600,240 360,300" fill="var(--orange)"/>
      <polygon points="0,330 360,300 360,312 0,343" fill="var(--white)"/>
    </svg>
    <h2 class="brand-name">Saffron<br>Lantern<br>Court</h2>
    <p class="holder-name">Harvinder Oberoi</p>
    <div class="holder-rule"></div>
    <div class="contact-rule"></div>
    <address class="contact">
      <div>7328 West Larkspur Rd</div>
      <div>Copperfield, Arizona, 85099</div>
      <div class="contact-line">
        <svg viewBox="0 0 12 12"><path d="M2.5 1l2 2-1 1.5c.6 1.4 1.6 2.4 3 3L8 6.5l2 2-1.2 1.8C5 10 2 7 1.7 3.2z"/></svg>
        (602) 555-0147
      </div>
      <div class="contact-line">
        <svg viewBox="0 0 12 12"><rect x="2" y="1" width="8" height="4"/><rect x="1" y="5" width="10" height="6" rx="1"/></svg>
        (602) 555-0193
      </div>
      <div class="contact-line">
        <svg viewBox="0 0 12 12"><circle cx="6" cy="6" r="5"/></svg>
        <span class="website">www.<span class="accent">SaffronLanternCourt</span>.example</span>
      </div>
    </address>
  </section>

</main>
</body>
</html>
```